Vantrel Web Services

This is a new It services company operating in Perth western Australia

we need a website that is easy to navigate without a cluttered feel to it it should have the following links and pages

About Us
Services
Clients
Contact Us
MY Vantrel (login for clients)

Hi it is a web based IT services company so we would expect customers to come to the website for 2 different purposes the first is to enquire about our services and then as they become customers come to our website to manage their services so whilst they are seperate we want do not want it to look like 2 different websites

hope this helps

Hi to update this we need a home page and templates for sub pages

this is a design brief only and not the coding of the pages or building of the site

```html
<!DOCTYPE html>
<html lang="en">
<head>
<meta charset="utf-8">
<title>Vantrel Web Services – About Us</title>
<link href="https://fonts.googleapis.com/css2?family=Arimo:wght@400;700&display=swap" rel="stylesheet">
<style>
  :root {
    --ink: #3a3a3a;
    --muted: #555;
    --page-bg: #f2f2f2;
    --red-top: #c8141a;
    --red-bottom: #8f0a0e;
    --navy: #0d1f7a;
    --panel: #ffffff;
    --box: #f2f2f2;
    --box-line: #d2d2d2;
    --footer: #363636;
    --footer-bar: #111;
    --footer-text: #e4e4e4;
    --photo-a: #1b8fd2;
    --photo-b: #2a3340;
  }
  * { box-sizing: border-box; margin: 0; padding: 0; }
  html, body { width: 933px; height: 1200px; overflow: hidden; }
  body { position: relative; font-family: "Arimo", Arial, sans-serif; color: var(--ink); background: var(--page-bg); }

  .backdrop { position: absolute; left: 0; top: 0; width: 933px; height: 1200px; }

  .logo-tab {
    position: absolute; left: 138px; top: 0; width: 189px; height: 85px;
    background: #fff; border-radius: 0 0 14px 14px;
    box-shadow: 0 3px 8px rgba(0,0,0,.35);
    display: flex; align-items: center; justify-content: center; gap: 9px;
  }
  .logo-tab .mark { width: 22px; height: 22px; border-radius: 50%; background: var(--red-top); }
  .logo-tab .name { font-size: 22px; font-weight: 700; color: var(--red-top); letter-spacing: .5px; }

  .phone {
    position: absolute; left: 585px; top: 16px; display: flex; align-items: center; gap: 8px;
    font-size: 25px; font-weight: 700; color: #555;
  }

  .main-nav {
    position: absolute; left: 126px; top: 102px; width: 681px; height: 32px;
    background: linear-gradient(var(--red-top), var(--red-bottom));
    border-radius: 6px 6px 0 0; display: flex;
  }
  .main-nav a {
    color: #fff; text-decoration: none; font-size: 13px; display: flex; align-items: center; justify-content: center;
    border-right: 1px solid rgba(0,0,0,.25); box-shadow: 1px 0 0 rgba(255,255,255,.18);
  }
  .main-nav a:last-child { border-right: 0; box-shadow: none; }

  .page-panel {
    position: absolute; left: 126px; top: 134px; width: 681px; height: 893px;
    background: var(--panel); border-radius: 0 0 8px 8px;
  }

  .team-photo {
    position: absolute; left: 151px; top: 162px; width: 411px; height: 120px;
    background: linear-gradient(180deg, var(--photo-a) 0%, #4fb1e4 45%, var(--photo-b) 100%);
  }

  .page-title { position: absolute; left: 160px; top: 291px; font-size: 17px; font-weight: 700; color: #444; }

  .article {
    position: absolute; left: 160px; top: 324px; width: 404px;
    font-size: 9px; line-height: 11.2px; letter-spacing: -0.1px; color: var(--muted);
  }
  .article p { text-indent: 14px; }
  .article p.flat { text-indent: 0; }
  .article .gap-s { margin-top: 11px; }

  .bullets { list-style: none; margin: 9px 0 6px; }
  .bullets li { position: relative; padding-left: 18px; height: 22.4px; }
  .bullets li::before { content: ""; position: absolute; left: 4px; top: 3px; width: 5px; height: 5px; background: #9a9a9a; }

  .contact-box {
    position: absolute; left: 581px; top: 162px; width: 198px; height: 165px;
    background: var(--box); border: 1px solid var(--box-line);
  }
  .contact-box h2 { position: absolute; left: 10px; top: 8px; font-size: 17px; font-weight: 700; color: #444; }
  .contact-box .details { position: absolute; left: 26px; top: 36px; font-size: 9.5px; line-height: 11px; color: var(--muted); white-space: pre; }
  .contact-box .cta {
    position: absolute; left: 60px; top: 133px; width: 77px; height: 23px; border-radius: 3px;
    background: var(--navy); color: #fff; font-size: 10px; display: flex; align-items: center; justify-content: center;
  }

  .site-footer { position: absolute; left: 0; top: 1013px; width: 933px; height: 161px; background: var(--footer); z-index: -1; }
  .footer-col { position: absolute; top: 1047px; font-size: 9.5px; line-height: 11.3px; color: var(--footer-text); white-space: pre; }
  .follow { position: absolute; left: 468px; top: 1113px; font-size: 9.5px; color: var(--footer-text); }
  .social { position: absolute; left: 468px; top: 1133px; display: flex; gap: 4px; }
  .social span { width: 14px; height: 14px; border-radius: 2px; }
  .newsletter-input {
    position: absolute; left: 602px; top: 1096px; width: 132px; height: 22px; background: #fff;
    border-radius: 3px; font-size: 10px; color: #333; padding: 5px 6px;
  }
  .newsletter-submit {
    position: absolute; left: 739px; top: 1096px; width: 64px; height: 22px;
    background: var(--red-top); color: #fff; font-size: 12px; display: flex; align-items: center; justify-content: center;
  }
  .consent-box { position: absolute; left: 604px; top: 1133px; width: 11px; height: 11px; background: #cfcfcf; }
  .consent { position: absolute; left: 624px; top: 1133px; font-size: 9.5px; line-height: 11px; color: var(--footer-text); white-space: pre; }
  .copyright {
    position: absolute; left: 0; top: 1174px; width: 933px; height: 26px; background: var(--footer-bar);
    color: #fff; font-size: 9.5px; display: flex; align-items: center; justify-content: center;
  }
</style>
</head>
<body>
  <svg class="backdrop" viewBox="0 0 933 1200" aria-hidden="true">
    <defs>
      <linearGradient id="head" x1="0" y1="0" x2="0" y2="1">
        <stop offset="0" stop-color="#ffffff"/><stop offset="1" stop-color="#d6d6d6"/>
      </linearGradient>
      <linearGradient id="band" x1="0" y1="0" x2="0" y2="1">
        <stop offset="0" stop-color="#6a6a6a"/><stop offset=".5" stop-color="#3e3e3e"/><stop offset="1" stop-color="#2c2c2c"/>
      </linearGradient>
    </defs>
    <rect x="0" y="0" width="933" height="70" fill="url(#head)"/>
    <path d="M0 70 H933 V374 Q466 300 0 374 Z" fill="url(#band)"/>
  </svg>

  <header>
    <div class="logo-tab"><span class="mark"></span><span class="name">Vantrel</span></div>
    <div class="phone">
      <svg width="20" height="26" viewBox="0 0 20 26" aria-hidden="true">
        <path d="M5 1 L9 1 L10 7 L7 9 Q8 15 12 19 L15 17 L19 20 L18 24 Q14 26 10 22 Q2 14 2 5 Q2 2 5 1 Z" fill="#b3141a"/>
      </svg>
      <span>(200) 5550 1187</span>
    </div>
    <nav class="main-nav">
      <a style="width:107px">Home</a>
      <a style="width:117px">About Us</a>
      <a style="width:111px">Services</a>
      <a style="width:110px">Clients</a>
      <a style="width:113px">Contact us</a>
      <a style="width:123px">Login</a>
    </nav>
  </header>

  <div class="page-panel"></div>

  <div class="team-photo" role="img" aria-label="Photo of the company team standing in a row against a blue backdrop"></div>

  <h1 class="page-title">About Us</h1>

  <article class="article">
    <p>Lorem ipsum dolor sit amet., consectetur adipiscing elit. set diem nonumy in convalis gravida neque. Nulla gravida vestibulum metis a acumsan, aliquam in sagitis ut. Solicitudin sed massa ud nim veniam. Curabitur tempus em vitae mi vestibulum volutpat malesuada erat vestibulum. set ali quam dolor at dolor consequat gravida. fusce mineque nec fequat sit amet. Tincidunt ut leo. Nam semper ornare enim.</p>
    <p>Lorem ipsum dolor sit amet, consecteteur adipiscing elit. sed diem nonumy inconvalis gravida neque. nulla gravida vestibulum metis a acumsan, aliquam in sagitis ut. solicitudin sed massa ud enim veniam. curabitur tempus em vitae mi vestibulum volutpat malesuada erat vestibulum.</p>

    <ul class="bullets">
      <li>Lorem ipsum dolor sit amet, consecteteur adipiscing elit, Sed diem nonumy inconvalis.</li>
      <li>Lorem ipsum dolor sit amet, consecteteur adipiscing elit. sed diem nonumy.</li>
      <li>Lorem ipsum dolor sit.</li>
      <li>Lorem ipsum dolor sit amet, consecteteur adipiscing elit.</li>
      <li>Lorem ipsum dolor.</li>
      <li>Lorem ipsum dolor sit amet, consectetur.</li>
      <li>Lorem ipsum dolor sit amet</li>
      <li>Lorem ipsum dolor sit amet.</li>
      <li>Lorem ipsum dolor sit amet.</li>
    </ul>

    <p>Lorem ipsum dolor sit amet. consecteteur adipiscing elit. Set diem nonumy inconvalis gravida neque. nulla gravida vestibulum metis a acumsan. Aliquam in sagitis ut. solicitudin sed massa ud nim veniam. Curabitur tempus em vitae.</p>
    <p class="flat">Mi vestibulum volutpat malesuada erat vestibulum. Sed aliquam dolor at dolor conseuat gravida. fusce mineque nec vequat sit amet. tincidunt ut leo. Nam semper ornare enim.</p>
    <p class="flat gap-s">Our Mission</p>
    <p class="flat gap-s">Lorem ipsum dolor sit amet, consecteteur adipiscing elit. Sed diem nonumy inconvalis gravida neque. Nulla gravida vestibulum metis a acumsan. Aliquam in sagitis ut.</p>
    <p class="flat gap-s">Our Vission</p>
    <p class="flat gap-s">Lorem ipsum dolor sit amet, consecteteur adipiscing elit. sed diem nonumy inconvalis gravida neque. Nulla gravida vestibulum metis a acumsan. Aliquam in sagitis ut. solicitudin sed massa ud nim veniam. curabitur tempus em vitae mi vestibulum volutpat malesuada erat vestibulum. sed ali quam dolor at dolor consequat gravida. Fusce mineque nec fequat sit amet. Tincidunt ut leo. Nam semper ornare enim.</p>
    <p class="gap-s">Lorem ipsum dolor sit amet, consecteteur adipiscing elit. Sed diem nonumy inconvalis gravida neque. Nulla gravida vestibulum metis a acumsan. aliquam in sagitis ut. Solicitudin sed massa ud enim veniam. curabitur tempus em vitae mi vestibulum volutpat malesuada erat vestibulum, sed aliquam dolor at dolor consewuat gravida. Fusce mineque nec fequat sit amet. tincidunt ut leo. Nam semper ornare enim.</p>
  </article>

  <aside class="contact-box">
    <h2>Contact Us</h2>
    <div class="details">lorem ipsum, 1238943,
lorem, Michigan, ZIPcode

Phone : XXX - XXXX - XXX
Fax     :  XXX - XXXX - XXXX
email   : info@vantrel.com</div>
    <div class="cta">Contact Now</div>
  </aside>

  <footer>
    <div class="site-footer"></div>
    <div class="footer-col" style="left:158px">Vantrel Web Services

Address :
lorem ipsum, 1238943,
lorem, Michigan, ZIPcode

Phone : XXX - XXXX - XXX
Fax     :  XXX - XXXX - XXXX
email   : info@vantrel.com</div>
    <div class="footer-col" style="left:334px">Home
About us
Services
Client
Blog
Latest News
Testimonials
Contact Us</div>
    <div class="footer-col" style="left:468px">Sitemap
Terms &amp; Conditions
Privacy Policy
Help</div>
    <div class="follow">Follow Us on &nbsp;:</div>
    <div class="social" aria-label="Social links">
      <span style="background:#3aa4d8"></span>
      <span style="background:#3b5b9a"></span>
      <span style="background:#e8821e"></span>
      <span style="background:#1f79b0"></span>
    </div>
    <div class="footer-col" style="left:600px">Receive our newsletter weekly.
We will never share your any information to the
3rd party.</div>
    <div class="newsletter-input">Your email address</div>
    <div class="newsletter-submit">SUBMIT</div>
    <div class="consent-box"></div>
    <div class="consent">by clicking this button, you agree
with our terms &amp; Conditions</div>
    <div class="copyright">Copyright &nbsp;©&nbsp; 2014, vantrel.com. All rights reserved.</div>
  </footer>
</body>
</html>
```